Letterhead Design for Law Firm

**Edit: I have added the photo of a bottom that I like.

------
We are looking for a re-design of our new letterhead. The letterhead is for a law firm and will be used for digital and traditionally printed correspondence.

Here are some suggestions:

- Please use colours are #8ec900 and simple black.
- Please do not use any type of "waves" at the bottom of the page. This is not in style at all.
- Please stay modern yet conservative.
- Please use font Segoe UI Light or similar if you can
- Avoid clipart or illustrations.
- Utilize ample white space in the layout so the design looks clean and information is easy to read at a glance. Don't overcrowd the letterhead.
- Make sure the letterhead design is consistent with our brand identity (see brambleford.ca)
-Please, no black headers or footers.

I am attaching my current letterhead and signature for your convenience.

Remember, the letterhead is an extension of our professional identity. We are a successful firm and trial lawyers who correspond with insurers, judges, lawyers, courts, clients, etc. Make it new, modern, attractive, yet powerful and conservative.

It needs to be easily printable. I would like the bleed removed in print so the black bar the bottom crosses the page (but the text is not near the edges)

Target Market(s)

Clients, Government Offices, Judiciary, Lawyers, Insurance Companies, Colleagues.

Industry/Entity Type

Law

Font styles to use
Other font styles liked:
• Segoe UI LIght, Calibri Light,

Colors
00AB8E
00BBA5
67D7C9
C6EFE9
E9F9F6

Requirements
Must have
• Everything that is on the letterhead now.
Nice to have
• Cutting Edge design, yet conservative.
Should not have
• law firm cliche design, images,

```html
<!DOCTYPE html>
<html lang="en">
<head>
<meta charset="utf-8">
<title>Harrow Personal Injury Lawyers – Letterhead</title>
<link href="https://fonts.googleapis.com/css2?family=Open+Sans:wght@300;400;600;700&display=swap" rel="stylesheet">
<style>
  :root {
    --brand-green: #80b83a;
    --brand-black: #0d0d0d;
    --ink: #1a1a1a;
    --ink-soft: #3a3a3a;
    --paper: #ffffff;
    --backdrop: #d9dadb;
  }
  * { box-sizing: border-box; margin: 0; padding: 0; }
  html, body {
    width: 1200px; height: 900px; overflow: hidden;
    background: var(--backdrop);
    font-family: "Open Sans", "Segoe UI", sans-serif;
    color: var(--ink);
  }
  .letterhead {
    position: absolute; left: 282px; top: 20px;
    width: 636px; height: 860px;
    background: var(--paper);
    overflow: hidden;
    box-shadow: 0 2px 10px rgba(0,0,0,.18);
  }

  /* Brand block */
  .brand-block {
    position: absolute; left: 0; top: 92px;
    width: 232px; height: 96px;
    background: var(--brand-black);
    border-radius: 0 12px 12px 0;
    display: flex; flex-direction: column; justify-content: center;
    padding-left: 40px;
  }
  .brand-rule { width: 158px; height: 1px; background: var(--brand-green); }
  .brand-name {
    color: #fff; font-weight: 400; font-size: 34px; letter-spacing: 1px;
    line-height: 1; margin: 6px 0 4px;
  }
  .brand-tagline {
    color: #fff; font-weight: 400; font-size: 8.6px; letter-spacing: 1.1px;
    margin-bottom: 5px;
  }

  /* Contact band */
  .contact-band {
    position: absolute; left: 246px; top: 40px; right: 0;
    height: 134px;
    background: var(--brand-green);
    border-radius: 0 0 0 12px;
    padding: 14px 0 0 16px;
  }
  .contact-list { list-style: none; }
  .contact-item {
    display: flex; align-items: center; gap: 8px;
    font-size: 11.5px; line-height: 1.25; color: var(--ink);
    margin-bottom: 6px;
  }
  .contact-icon {
    width: 20px; height: 20px; border-radius: 50%;
    background: var(--brand-black);
    display: flex; align-items: center; justify-content: center;
    flex: none;
  }
  .contact-icon svg { width: 12px; height: 12px; }
  .clerk-details {
    position: absolute; left: 306px; top: 186px;
    font-size: 11.5px; line-height: 1.35; color: var(--ink-soft);
  }

  /* Practice areas */
  .practice-areas {
    position: absolute; right: 58px; top: 594px;
    text-align: right; font-size: 11.5px; line-height: 1.3; color: var(--ink-soft);
  }
  .practice-title { font-weight: 700; color: var(--ink); }
  .side-bar {
    position: absolute; right: 0; top: 580px;
    width: 40px; height: 142px;
    background: var(--brand-black);
    border-radius: 10px 0 0 10px;
  }

  /* Sign-off */
  .sign-off {
    position: absolute; left: 60px; top: 640px;
    font-size: 10.5px; line-height: 1.4; color: var(--ink-soft);
  }
  .sign-off strong { color: var(--ink); font-weight: 700; }
  .signature {
    width: 150px; height: 46px; margin: 8px 0 6px 14px;
    background: linear-gradient(90deg, #e6e6e6, #f3f3f3);
    border-radius: 4px;
  }

  /* Footer band */
  .footer-band {
    position: absolute; left: 0; bottom: 16px;
    width: 560px; height: 30px;
    background: var(--brand-green);
    border-radius: 0 10px 10px 0;
  }
</style>
</head>
<body>
  <main class="letterhead">
    <div class="brand-block">
      <div class="brand-rule"></div>
      <div class="brand-name">HARROW</div>
      <div class="brand-tagline">PERSONAL INJURY LAWYERS</div>
      <div class="brand-rule"></div>
    </div>

    <div class="contact-band">
      <ul class="contact-list">
        <li class="contact-item">
          <span class="contact-icon"><svg viewBox="0 0 12 12" fill="none" stroke="#80b83a" stroke-width="1"><circle cx="6" cy="6" r="5"/><ellipse cx="6" cy="6" rx="2.2" ry="5"/><line x1="1" y1="6" x2="11" y2="6"/></svg></span>
          www.BRAMBLEFORD.ca
        </li>
        <li class="contact-item">
          <span class="contact-icon"><svg viewBox="0 0 12 12" fill="#80b83a"><path d="M2.5 1.5l2 .2 1 2.5-1.2 1a6 6 0 0 0 2.5 2.5l1-1.2 2.5 1 .2 2c-4.5.6-8.6-3.5-8-8z"/></svg></span>
          555-210-4400
        </li>
        <li class="contact-item">
          <span class="contact-icon"><svg viewBox="0 0 12 12" fill="none" stroke="#80b83a" stroke-width="1"><rect x="1.5" y="4.5" width="9" height="5" rx="1"/><rect x="3.5" y="1.5" width="5" height="3"/><line x1="3.5" y1="7.5" x2="8.5" y2="7.5"/></svg></span>
          555-210-4401
        </li>
        <li class="contact-item">
          <span class="contact-icon"><svg viewBox="0 0 12 12" fill="#80b83a"><path d="M6 1a3.5 3.5 0 0 1 3.5 3.5C9.5 7 6 11 6 11S2.5 7 2.5 4.5A3.5 3.5 0 0 1 6 1zm0 2a1.5 1.5 0 1 0 0 3 1.5 1.5 0 0 0 0-3z"/></svg></span>
          <span>40 Mill Street E., Suite 1200<br>Westbrook, ON K2R 3B7</span>
        </li>
      </ul>
    </div>

    <p class="clerk-details">File Clerk: Clara Whitfield<br>Email: clara@brambleford.ca</p>

    <section class="practice-areas">
      <p class="practice-title">Practice Restricted</p>
      <p>Serious Personal Injury</p>
      <p>Wrongful Death Litigation</p>
      <p>Long-Term Disability Litigation</p>
      <p>Wrongful Dismissal Litigation</p>
      <p>Employee Terminations</p>
    </section>
    <div class="side-bar"></div>

    <section class="sign-off">
      <p>Yours very truly,</p>
      <p><strong>HARROW PERSONAL INJURY LAWYERS</strong></p>
      <div class="signature" role="img" aria-label="Handwritten signature of Owen T. Harrow"></div>
      <p>Owen T. Harrow</p>
      <p><strong>Harrow Law Professional Corporation</strong></p>
      <p>/cw</p>
      <p>Encl</p>
    </section>

    <div class="footer-band"></div>
  </main>
</body>
</html>
```